Veltrano - Mechanic/Collision Center Business Card

We're looking for a business card design for our mechanic/ collision repair shop.

Can be with colours or monochromatic.

See the attached files.

Many thanks

```html
<!DOCTYPE html>
<html lang="pt">
<head>
<meta charset="utf-8">
<title>Veltrano – Business Card</title>
<link rel="stylesheet" href="https://fonts.googleapis.com/css2?family=Montserrat:wght@800&family=Arimo:wght@400&display=swap">
<style>
  :root {
    --backdrop: #3d4049;
    --card-black: #1b1e22;
    --brand-blue: #1f9bd7;
    --deep-blue: #0f6f9e;
    --paper: #ffffff;
    --silver: #c9cacc;
    --ink: #15181b;
  }
  * { margin: 0; padding: 0; box-sizing: border-box; }
  html, body { width: 1200px; height: 675px; overflow: hidden; background: var(--backdrop); }
  .stage { position: relative; width: 1200px; height: 675px; }
  .card {
    position: absolute; top: 194px; width: 500px; height: 286px;
    overflow: hidden; border-radius: 3px;
    box-shadow: 0 14px 30px rgba(0,0,0,.35);
  }
  .card-front { left: 70px; background: var(--paper); }
  .card-back { left: 630px; background: var(--card-black); }
  .card svg.card-art { position: absolute; inset: 0; }

  .brand-name {
    position: absolute; font-family: "Montserrat", sans-serif; font-weight: 800;
    letter-spacing: 1px; text-transform: uppercase;
  }
  .card-front .brand-name { top: 18px; left: 24px; font-size: 26px; color: var(--ink); }
  .card-back .brand-name {
    top: 50%; left: 50%; transform: translate(-50%, -50%);
    font-size: 50px; color: var(--paper);
  }
  .brand-mark {
    display: inline-block; width: 14px; height: 14px; border-radius: 50%;
    background: var(--brand-blue); margin-right: 8px; vertical-align: 3px;
  }

  .name-tag {
    position: absolute; top: 112px; right: 0; height: 34px; padding: 0 26px 0 20px;
    background: var(--ink); color: var(--paper);
    font-family: "Montserrat", sans-serif; font-weight: 800; font-size: 19px;
    letter-spacing: 1px; line-height: 34px; text-transform: uppercase;
  }
  .contact-list {
    position: absolute; top: 156px; right: 24px; list-style: none;
    font-family: "Arimo", sans-serif; font-size: 12.5px; color: var(--ink); line-height: 1.3;
  }
  .contact-list li { display: flex; align-items: flex-start; margin-bottom: 5px; }
  .contact-icon {
    flex: none; width: 15px; height: 15px; border-radius: 50%;
    background: var(--ink); margin-right: 7px; margin-top: 0;
    display: flex; align-items: center; justify-content: center;
  }
  .contact-icon svg { width: 9px; height: 9px; }
</style>
</head>
<body>
<main class="stage">

  <section class="card card-front" aria-label="Card front">
    <svg class="card-art" width="500" height="286" viewBox="0 0 500 286">
      <defs>
        <linearGradient id="carShade" x1="0" y1="0" x2="1" y2="1">
          <stop offset="0" stop-color="#d8d9db"/>
          <stop offset="1" stop-color="#bfc0c3"/>
        </linearGradient>
      </defs>
      <rect class="car-illustration" x="0" y="56" width="300" height="120" fill="url(#carShade)" role="img" aria-label="Grey car silhouette illustration"/>
      <polygon class="blue-field" points="500,0 500,286 60,286 175,150 300,150 345,96 500,96" fill="var(--brand-blue)"/>
      <polygon class="blue-field" points="330,0 500,0 500,96 300,96" fill="var(--brand-blue)"/>
      <polygon class="blue-stripe" points="0,205 110,88 360,60 338,82 124,104 0,236" fill="var(--brand-blue)"/>
      <polygon class="black-chevron" points="0,286 0,250 120,118 360,100 320,150 175,150 60,286" fill="var(--card-black)"/>
      <path class="deep-wave" d="M500,210 C430,230 400,250 390,286 L500,286 Z" fill="var(--deep-blue)"/>
    </svg>

    <div class="brand-name"><span class="brand-mark"></span>Veltrano</div>
    <div class="name-tag">Rui Almeida</div>

    <ul class="contact-list">
      <li>
        <span class="contact-icon"><svg viewBox="0 0 10 10"><path d="M5 0.5a3 3 0 0 1 3 3c0 2.3-3 6-3 6s-3-3.7-3-6a3 3 0 0 1 3-3z" fill="#fff"/><circle cx="5" cy="3.5" r="1.1" fill="#15181b"/></svg></span>
        <span>Veltrano, LDA<br>Rua das Oficinas, 42<br>1900-215 Lisboa</span>
      </li>
      <li>
        <span class="contact-icon"><svg viewBox="0 0 10 10"><path d="M2 1l2 0.4 0.6 2-1.2 1a6 6 0 0 0 2.6 2.6l1-1.2 2 0.6L9 8.4C8.6 9.3 7.5 9.5 6.6 9.1 4 8 2 6 0.9 3.4 0.5 2.5 0.8 1.4 2 1z" fill="#fff"/></svg></span>
        <span>+351 910555204</span>
      </li>
      <li>
        <span class="contact-icon"><svg viewBox="0 0 10 10"><rect x="1" y="2.5" width="8" height="5" fill="#fff"/><path d="M1 2.5l4 3 4-3" stroke="#15181b" stroke-width="0.8" fill="none"/></svg></span>
        <span>veltrano.mail@example.com</span>
      </li>
      <li>
        <span class="contact-icon"></span>
        <span>www.veltrano-auto.pt</span>
      </li>
    </ul>
  </section>

  <section class="card card-back" aria-label="Card back">
    <svg class="card-art" width="500" height="286" viewBox="0 0 500 286">
      <polyline class="frame-bracket" points="410,52 150,52 60,180" fill="none" stroke="var(--brand-blue)" stroke-width="24" stroke-linejoin="miter"/>
      <polyline class="frame-bracket" points="90,234 350,234 440,106" fill="none" stroke="var(--brand-blue)" stroke-width="24" stroke-linejoin="miter"/>
    </svg>
    <div class="brand-name">Veltrano</div>
  </section>

</main>
</body>
</html>
```